Easy - Fix our "Win a Party" Promo Flyer

Please see attached promo flyer with all the information required. Looking for quick assistance so we can go live with the advertising for this competition. Looking for something more commercial and polished. Very attractive so that lots of people enter the competition. <br/><br/>Happy for it to look a little bit festive as the competition is running in December. <br/><br/>Attached is out Grill Kammer Logo and first attempts at poster. Please let me know if you need anything further. <br/><br/>If you see any grammar or spelling errors please feel free to fix too.
Corporate Businesses who are buying vouchers as staff christmas gifts/bonus

```html
<!DOCTYPE html>
<html lang="en">
<head>
<meta charset="utf-8">
<title>Win the Ultimate Staff Party – Grill Kammer</title>
<link rel="stylesheet" href="https://fonts.googleapis.com/css2?family=Oswald:wght@400;500;600;700&family=Open+Sans:ital,wght@0,400;0,600;1,400;1,600&family=Dancing+Script:wght@500;700&display=swap">
<style>
  :root {
    --ink-dark: #111111;
    --panel-dark: #1c1c1c;
    --red-deep: #8e0a10;
    --red-main: #c8141c;
    --red-bright: #e2262c;
    --gold-light: #f4d98a;
    --gold-main: #d6a545;
    --gold-deep: #a87a24;
    --cream: #f6ead0;
    --white: #ffffff;
    --brand-red: #e31b23;
  }
  * { margin: 0; padding: 0; box-sizing: border-box; }
  html, body { width: 938px; height: 1200px; overflow: hidden; background: #e9e6e1; }
  .flyer { position: relative; width: 938px; height: 1200px; overflow: hidden; font-family: "Open Sans", sans-serif; }

  .side-panel {
    position: absolute; left: 0; top: 0; width: 354px; height: 1200px;
    background: radial-gradient(ellipse at 50% 30%, #3a3a3a 0%, var(--panel-dark) 55%, var(--ink-dark) 100%);
  }
  .balloon-art {
    position: absolute; left: 30px; top: 150px; width: 324px; height: 480px;
    background: radial-gradient(circle at 45% 20%, rgba(230,190,90,.75) 0%, rgba(180,180,180,.45) 35%, rgba(40,40,40,.2) 65%, transparent 80%);
  }
  .side-greeting {
    position: absolute; left: 0; width: 354px; top: 820px; text-align: center;
    font-family: "Dancing Script", cursive; font-weight: 700; font-size: 34px; line-height: 50px; color: var(--gold-main);
  }
  .brand-mark { position: absolute; left: 0; width: 354px; top: 960px; text-align: center; }
  .brand-mark .dot { display: block; width: 46px; height: 46px; border-radius: 50%; background: var(--brand-red); margin: 0 auto 14px; }
  .brand-mark .name {
    font-family: "Oswald", sans-serif; font-weight: 600; font-size: 52px; line-height: 56px; color: var(--white); text-transform: uppercase;
  }

  .main-panel {
    position: absolute; left: 354px; top: 0; width: 584px; height: 1200px;
    background: radial-gradient(ellipse at 60% 40%, var(--red-bright) 0%, var(--red-main) 45%, var(--red-deep) 100%);
    color: var(--white);
  }
  .headline-win {
    position: absolute; left: 42px; top: 40px; white-space: nowrap;
    font-family: "Oswald", sans-serif; font-weight: 700; font-size: 160px; line-height: 160px; letter-spacing: -2px;
    background: linear-gradient(180deg, var(--gold-light), var(--gold-main) 55%, var(--gold-deep));
    -webkit-background-clip: text; background-clip: text; color: transparent;
  }
  .headline-sub {
    position: absolute; left: 268px; top: 160px; white-space: nowrap;
    font-family: "Oswald", sans-serif; font-weight: 400; font-size: 36px; line-height: 40px; color: var(--white);
  }
  .headline-main {
    position: absolute; left: 40px; width: 504px; top: 232px; white-space: nowrap;
    font-family: "Oswald", sans-serif; font-weight: 600; font-size: 104px; line-height: 124px; letter-spacing: 0;
    color: var(--cream); text-shadow: 0 4px 8px rgba(0,0,0,.35);
  }
  .gold-rule { position: absolute; left: 42px; top: 372px; width: 500px; height: 3px; background: linear-gradient(90deg, var(--gold-deep), var(--gold-light), var(--gold-main)); }
  .tagline {
    position: absolute; left: 0; width: 584px; top: 396px; text-align: center; white-space: nowrap;
    font-family: "Dancing Script", cursive; font-weight: 700; font-size: 44px; line-height: 52px; color: var(--gold-main);
  }
  .offer {
    position: absolute; left: 30px; width: 524px; text-align: center;
    font-family: "Oswald", sans-serif; font-weight: 500; font-size: 25px; line-height: 33px; text-transform: uppercase;
  }
  .offer-top { top: 512px; }
  .offer-bottom { top: 620px; }
  .deadline-ribbon {
    position: absolute; left: 110px; top: 560px; width: 314px; height: 40px;
    background: linear-gradient(90deg, var(--gold-deep), var(--gold-light) 50%, var(--gold-deep));
    clip-path: polygon(0 0, 100% 0, 96% 50%, 100% 100%, 0 100%, 4% 50%);
    text-align: center; font-family: "Oswald", sans-serif; font-weight: 500; font-size: 24px; line-height: 40px; color: var(--white);
  }
  .prize-details {
    position: absolute; left: 30px; width: 524px; top: 756px; text-align: center;
    font-style: italic; font-weight: 600; font-size: 19px; line-height: 30px; color: var(--gold-main);
  }
  .prize-details p + p { margin-top: 8px; }
  .voucher-row { position: absolute; left: 40px; top: 932px; display: flex; gap: 12px; }
  .voucher { width: 164px; height: 58px; border: 2px solid var(--white); }
  .voucher-kraft { background: linear-gradient(90deg, #c9a36a, #e6cfa2); }
  .voucher-yellow { background: linear-gradient(90deg, #f2c21b, #f7e27a); }
  .voucher-red { background: linear-gradient(90deg, #d7262b, #f4f0ea 40%); }
  .tip {
    position: absolute; left: 0; width: 584px; top: 1032px; text-align: center;
    font-size: 16px; line-height: 22px; text-transform: uppercase;
  }
  .fine-print { position: absolute; left: 30px; width: 524px; top: 1058px; text-align: center; font-size: 13px; line-height: 20px; }
  .contact-row {
    position: absolute; left: 30px; width: 524px; top: 1144px; display: flex; justify-content: space-between; align-items: center;
    font-size: 14px;
  }
  .contact-item { display: flex; align-items: center; gap: 8px; }
  .contact-item svg { width: 16px; height: 16px; }
</style>
</head>
<body>
<div class="flyer">
  <aside class="side-panel">
    <div class="balloon-art" role="img" aria-label="Cluster of gold, silver and black party balloons with falling gold confetti"></div>
    <p class="side-greeting">Have a Grilly Xmas<br>at The Grill Kammer</p>
    <div class="brand-mark">
      <span class="dot"></span>
      <div class="name">Grill<br>Kammer</div>
    </div>
  </aside>

  <main class="main-panel">
    <div class="headline-win">WIN</div>
    <div class="headline-sub">THE ULTIMATE</div>
    <h1 class="headline-main">STAFF PARTY</h1>
    <div class="gold-rule"></div>
    <p class="tagline">For you and your colleagues</p>

    <p class="offer offer-top">Purchase K5,000 worth of vouchers before</p>
    <div class="deadline-ribbon">DECEMBER 31ST</div>
    <p class="offer offer-bottom">And go into the draw to win the ultimate staff party for 150 people!</p>

    <div class="prize-details">
      <p>This includes a venue, BBQ-style PNG menu,<br>roast pig, decor &amp; much more...</p>
      <p>We'll even throw in an extra large themed cake<br>with your company logo on it!</p>
    </div>

    <div class="voucher-row">
      <div class="voucher voucher-kraft" role="img" aria-label="Kraft paper shopping voucher sample"></div>
      <div class="voucher voucher-yellow" role="img" aria-label="Yellow shopping voucher sample"></div>
      <div class="voucher voucher-red" role="img" aria-label="Red and white shopping voucher sample"></div>
    </div>

    <p class="tip">Tip: buy more vouchers to have better chances of winning</p>
    <p class="fine-print">*For every HR department enquiry we receive, a special surprise will be given,<br>so HURRY and contact us below on...</p>

    <div class="contact-row">
      <span class="contact-item">
        <svg viewBox="0 0 16 16"><rect x="1" y="3" width="14" height="10" rx="1" fill="none" stroke="#f4d98a" stroke-width="1.5"/><path d="M1 4l7 5 7-5" fill="none" stroke="#f4d98a" stroke-width="1.5"/></svg>
        sales@embergrillco.com.pg
      </span>
      <span class="contact-item">
        <svg viewBox="0 0 16 16"><path d="M4 1l3 3-2 2c1 2 3 4 5 5l2-2 3 3-2 2C7 14 2 9 2 3z" fill="#f4d98a"/></svg>
        7150 33800
      </span>
      <span class="contact-item">
        <svg viewBox="0 0 16 16"><circle cx="8" cy="8" r="7" fill="#f4d98a"/></svg>
        grillkammerpng
      </span>
    </div>
  </main>
</div>
</body>
</html>
```